Brent Oakes Director / Photographer Branding

I need note pads, envelops, business cards and letter head for my company. I'm a fashion and advertising director / photographer. I'm having trouble deciding how to include both Director & Photographer in my title or if it is even necessary. Maybe just my name is enough. I'm open for even using my initials if it works with the design and overall pieces. Please view my website to see what I have at this moment and what work I do. www.brentoakesstudio-mail.net
Updates

Project Deadline Extended
Reason: Hello Everyone! I'm extending the deadline since I have been traveling on a job out of country and I wanted to have more time to look through all the designs and give enough time for everyone to provide changes with designs and updates. I will be more available to communicate online now that I'm back in the office! Thank you! Brent Oakes

Target Market(s)

Fashion magazines, clothing lines and beauty cosmetic brands.

Industry/Entity Type

Fashion Photography

Font styles to use
Sans Serif

Colors
acd036
acd35d
cbcbcb
f5f5f5

Requirements
Must have
• My name.. Brent Oakes, my website: brentoakesstudio-mail.net my phone number, 555-284-6103
• I don't need my address on these. I also live by the philosophy that less is more and keeping things simple ads strength to a design. I also don't want to stop people from taking chances and experimenting with an idea that might take me down different road with my branding.
Nice to have
• Bold designs and clean lines. I'm open to ideas that I could adopt but I lean towards a more minimalistic look in general.
Should not have
• Not have cheesy graphics or pictures. No images of cameras, film or anything that looks like it is a camera or aperture, lens etc... ;)

```html
<!DOCTYPE html>
<html lang="en">
<head>
<meta charset="utf-8">
<title>Brent Oakes — Business Cards</title>
<link rel="stylesheet" href="https://fonts.googleapis.com/css2?family=Questrial&display=swap">
<style>
  :root {
    --backdrop: #b9b9b9;
    --card: #1b1b1c;
    --pattern-zone: #101011;
    --ink-white: #f5f5f5;
    --ink-grey: #cbcbcb;
    --ink-muted: #a9a9a9;
  }
  * { margin: 0; padding: 0; box-sizing: border-box; }
  html, body { width: 1200px; height: 859px; overflow: hidden; }
  body {
    background: var(--backdrop);
    font-family: "Questrial", "Century Gothic", sans-serif;
    position: relative;
  }
  .card {
    position: absolute;
    width: 575px;
    height: 328px;
    background: var(--card);
    border-radius: 14px;
    overflow: hidden;
  }
  .card--front { left: 107px; top: 89px; }
  .card--back { left: 512px; top: 451px; }

  /* Front */
  .front-mark {
    position: absolute;
    left: 139px; top: 140px;
    width: 40px; height: 40px;
    border: 4px solid var(--ink-white);
    border-radius: 50%;
  }
  .front-divider {
    position: absolute;
    left: 196px; top: 128px;
    width: 3px; height: 64px;
    background: var(--ink-white);
  }
  .front-name {
    position: absolute;
    left: 212px; top: 130px;
    font-size: 31px;
    color: var(--ink-white);
    line-height: 1;
  }
  .front-title {
    position: absolute;
    left: 237px; top: 172px;
    font-size: 13px;
    color: var(--ink-grey);
    letter-spacing: 0.3px;
  }

  /* Back */
  .pattern-zone { position: absolute; left: 0; top: 0; }
  .back-mark {
    position: absolute;
    left: 481px; top: 33px;
    width: 52px; height: 52px;
    border: 5px solid var(--ink-white);
    border-radius: 50%;
  }
  .back-divider {
    position: absolute;
    left: 322px; top: 169px;
    width: 2px; height: 122px;
    background: var(--ink-muted);
  }
  .identity { position: absolute; left: 332px; top: 167px; }
  .identity__name { font-size: 17px; color: var(--ink-white); line-height: 1.1; }
  .identity__title { font-size: 12px; color: var(--ink-grey); margin-top: 2px; }
  .contact-list {
    position: absolute;
    left: 332px; top: 214px;
    list-style: none;
  }
  .contact-list li {
    display: flex; align-items: center; gap: 5px;
    font-size: 12.5px;
    color: var(--ink-white);
    height: 18px;
  }
  .contact-list svg { width: 10px; height: 10px; flex: none; }
  .social-list {
    position: absolute;
    right: calc(575px - 314px);
    top: 244px;
    list-style: none;
    text-align: right;
  }
  .social-list li {
    font-size: 12px;
    color: var(--ink-muted);
    height: 16px;
    line-height: 16px;
  }
</style>
</head>
<body>
  <section class="card card--front" aria-label="Business card front">
    <span class="front-mark"></span>
    <span class="front-divider"></span>
    <p class="front-name">Brent Oakes</p>
    <p class="front-title">Director / Photographer</p>
  </section>

  <section class="card card--back" aria-label="Business card back">
    <svg class="pattern-zone" width="575" height="328" viewBox="0 0 575 328" role="img" aria-label="Repeating monogram pattern area">
      <polygon points="0,0 489,0 88,328 0,328" fill="var(--pattern-zone)"/>
    </svg>
    <span class="back-mark"></span>
    <span class="back-divider"></span>
    <div class="identity">
      <p class="identity__name">BRENT OAKES</p>
      <p class="identity__title">Director / Photographer</p>
    </div>
    <ul class="contact-list">
      <li>
        <svg viewBox="0 0 10 10" aria-hidden="true"><rect x="2" y="0.5" width="6" height="9" rx="1" fill="none" stroke="var(--ink-white)" stroke-width="1.2"/></svg>
        555-284-6103
      </li>
      <li>
        <svg viewBox="0 0 10 10" aria-hidden="true"><rect x="0.5" y="2" width="9" height="6" fill="var(--ink-white)"/><polyline points="0.5,2 5,5.5 9.5,2" fill="none" stroke="var(--card)" stroke-width="1"/></svg>
        brent@brentoakesstudio-mail.net
      </li>
      <li>
        <svg viewBox="0 0 10 10" aria-hidden="true"><circle cx="5" cy="5" r="4.3" fill="none" stroke="var(--ink-white)" stroke-width="1"/><ellipse cx="5" cy="5" rx="1.8" ry="4.3" fill="none" stroke="var(--ink-white)" stroke-width="0.8"/><line x1="0.7" y1="5" x2="9.3" y2="5" stroke="var(--ink-white)" stroke-width="0.8"/></svg>
        www.brentoakesstudio-mail.net
      </li>
    </ul>
    <ul class="social-list">
      <li>brentoakesphotography</li>
      <li>@brentoakesdotcom</li>
      <li>@brentoakes</li>
    </ul>
  </section>
</body>
</html>
```